Modern Brochure Design for Music School !!

I would like to have a brochure (A4 two fold) created for my partners music school. I would like it to incorporate information from his website, showing what classes are taught (singing lessons, drum lessons, guitar lessons and keyboard lessons). I would like to keep the same font style or as close to what's on the website if possible.

It needs to grab attention and be modern in design to attract age group of 18-35 while briefly detailing what services they provide, including their location and phone number

Info can all be found on the website www.themelodyloft.com.au

Target Market(s)

18-35 y/o

Industry/Entity Type

School

Font styles to use
Serif

Colors
000000

Requirements
Must have
• Key content from website
• List of classes (singing, drums, guitar, keyboard)
• Address / phone number
• Find us on Facebook - The Melody Loft /Follow @the_melody_loft
• Mention - gift vouchers available
• Black and white colours preferably no bright colours (like website)
• Modern and professional please!!
Nice to have
• Same type font as website or close to
• Not too much content
Should not have
• .

```html
<!DOCTYPE html>
<html lang="en">
<head>
<meta charset="utf-8">
<title>The Melody Loft – Flyer</title>
<link rel="stylesheet" href="https://fonts.googleapis.com/css2?family=Arimo&family=Delius&family=Montserrat:wght@400;700&family=Oswald:wght@400;700&family=Roboto+Condensed&display=swap">
<style>
  :root {
    --page-bg: #e9e7e4;
    --divider-red: #7c1c12;
    --ink: #ffffff;
    --dark: #111111;
    --circle-dark: #232323;
  }
  html, body {
    margin: 0; padding: 0;
    width: 1200px; height: 1200px;
    overflow: hidden;
    background: var(--page-bg);
  }
  .canvas { position: relative; width: 1200px; height: 1200px; }
  .flyer {
    position: absolute; left: 187px; top: 21px;
    width: 1032px; height: 1447px;
    transform: scale(0.8); transform-origin: 0 0;
    background: var(--divider-red);
    overflow: hidden;
    box-shadow: 0 6px 24px rgba(0,0,0,.35);
  }
  .tile { position: absolute; }
  .tile--cymbal { left: 0; top: 0; width: 395px; height: 435px; background: linear-gradient(160deg,#3a2a1c 0%,#a07a48 40%,#5a3a24 75%,#2a1a12 100%); }
  .tile--acoustic { left: 403px; top: 0; width: 312px; height: 435px; background: radial-gradient(circle at 60% 40%,#c46a3c 0%,#8a3a1e 45%,#3a1408 100%); }
  .tile--keys { left: 723px; top: 0; width: 309px; height: 435px; background: linear-gradient(200deg,#111 0%,#555 45%,#cfcfcf 80%,#888 100%); }
  .tile--kit { left: 0; top: 442px; width: 395px; height: 332px; background: linear-gradient(180deg,#2a2a2a 0%,#8a8478 45%,#3a3530 100%); }
  .tile--mic { left: 0; top: 781px; width: 395px; height: 300px; background: radial-gradient(circle at 20% 25%,#ffd27a 0%,#d07020 30%,#7a2a0c 70%,#3a1004 100%); }
  .tile--vocalist { left: 723px; top: 442px; width: 309px; height: 639px; background: linear-gradient(170deg,#1a1a3a 0%,#3a3a6a 35%,#1a1a2a 70%,#3a1a2a 100%); }
  .tile--drummer { left: 0; top: 1088px; width: 395px; height: 359px; background: radial-gradient(circle at 55% 30%,#e8c070 0%,#a07030 45%,#3a2410 100%); }
  .tile--piano { left: 403px; top: 1088px; width: 312px; height: 359px; background: linear-gradient(180deg,#222 0%,#8a8a8a 35%,#333 70%,#111 100%); }
  .tile--electric { left: 723px; top: 1088px; width: 309px; height: 359px; background: linear-gradient(200deg,#2a0c08 0%,#7a2418 45%,#1a0604 100%); }

  .banner { position: absolute; left: 0; top: 0; width: 1032px; height: 180px; }
  .banner__title {
    position: absolute; left: 25px; top: 28px; margin: 0;
    font-family: "Oswald", sans-serif; font-weight: 400;
    font-size: 58px; letter-spacing: 1px; color: var(--ink);
    transform: scaleX(0.82); transform-origin: left center;
  }

  .voucher {
    position: absolute; left: 797px; top: 115px; width: 160px; height: 158px;
    background: #fff; box-sizing: border-box;
    outline: 2px dashed #222; outline-offset: -6px;
    display: flex; align-items: center; justify-content: center; text-align: center;
    font-family: "Roboto Condensed", sans-serif; font-size: 33px; line-height: 1.28; color: #111;
  }

  .badge {
    position: absolute; left: 103px; top: 369px; width: 832px; height: 771px;
    border-radius: 50%; box-sizing: border-box;
    border: 9px solid #fff;
    background: radial-gradient(circle at 50% 45%,#2e2e2e 0%,var(--circle-dark) 55%,#151515 100%);
    color: var(--ink); text-align: center;
  }
  .badge__name {
    position: absolute; left: 0; right: 0; top: 78px; margin: 0;
    font-family: "Oswald", sans-serif; font-weight: 700; text-transform: uppercase;
    font-size: 86px; line-height: 1.04; letter-spacing: 2px;
  }
  .badge__tagline {
    position: absolute; left: 0; right: 0; top: 378px; margin: 0;
    font-family: "Delius", cursive; font-size: 42px;
  }
  .lessons {
    position: absolute; left: 205px; top: 448px; margin: 0; padding: 0; list-style: none;
    text-align: left; font-family: "Arimo", sans-serif; font-size: 37px; line-height: 61px;
  }
  .lessons li { display: flex; align-items: center; gap: 8px; }
  .lessons svg { width: 26px; height: 26px; }

  .info {
    position: absolute; left: 110px; top: 1238px; width: 805px; height: 180px;
    box-sizing: border-box; border: 2px solid #fff; border-radius: 90px;
    background: rgba(0,0,0,.72); color: var(--ink); text-align: center;
    font-family: "Montserrat", sans-serif;
  }
  .info__motto { margin: 18px 0 0; font-weight: 700; font-size: 20px; line-height: 28px; letter-spacing: .5px; }
  .info__row {
    display: flex; justify-content: center; align-items: center; gap: 26px;
    font-size: 17.5px; margin-top: 16px;
  }
  .info__row--small { font-size: 16px; margin-top: 14px; }
  .info__item { display: flex; align-items: center; gap: 8px; }
  .info__item svg { width: 20px; height: 20px; }
</style>
</head>
<body>
<div class="canvas">
  <div class="flyer">
    <div class="tile tile--cymbal" role="img" aria-label="Photo of a drumstick striking a cymbal"></div>
    <div class="tile tile--acoustic" role="img" aria-label="Photo of hands strumming an acoustic guitar"></div>
    <div class="tile tile--keys" role="img" aria-label="Black and white photo of hands playing piano keys"></div>
    <div class="tile tile--kit" role="img" aria-label="Photo of a drum kit with cymbals"></div>
    <div class="tile tile--mic" role="img" aria-label="Photo of a vintage microphone under warm stage lights"></div>
    <div class="tile tile--vocalist" role="img" aria-label="Photo of a singer performing into a microphone"></div>
    <div class="tile tile--drummer" role="img" aria-label="Photo of a drummer performing on stage"></div>
    <div class="tile tile--piano" role="img" aria-label="Black and white close-up photo of piano keys"></div>
    <div class="tile tile--electric" role="img" aria-label="Photo of an electric guitar neck in red light"></div>

    <svg class="banner" viewBox="0 0 1032 180" aria-hidden="true">
      <path d="M0 0 H640 C600 60 560 130 480 140 H0 Z" fill="#111"/>
      <path d="M0 140 H480 C560 130 600 60 640 0" fill="none" stroke="#fff" stroke-width="2.5"/>
    </svg>
    <h2 class="banner__title">TEACHING IS OUR PASSION</h2>

    <div class="voucher">Gift<br>vouchers<br>available</div>

    <section class="badge">
      <h1 class="badge__name">The<br>Melody<br>Loft</h1>
      <p class="badge__tagline">Be Prepared! Be Professional!</p>
      <ul class="lessons">
        <li><svg viewBox="0 0 24 24"><path d="M3 13 L9 19 L21 5" fill="none" stroke="#fff" stroke-width="3.5"/></svg>SINGING LESSONS</li>
        <li><svg viewBox="0 0 24 24"><path d="M3 13 L9 19 L21 5" fill="none" stroke="#fff" stroke-width="3.5"/></svg>DRUM LESSONS</li>
        <li><svg viewBox="0 0 24 24"><path d="M3 13 L9 19 L21 5" fill="none" stroke="#fff" stroke-width="3.5"/></svg>GUITAR LESSONS</li>
        <li><svg viewBox="0 0 24 24"><path d="M3 13 L9 19 L21 5" fill="none" stroke="#fff" stroke-width="3.5"/></svg>KEYBOARD LESSONS</li>
      </ul>
    </section>

    <footer class="info">
      <p class="info__motto">WE STRIVE TO MAKE THE WORLD A NICER PLACE TO BE IN<br>ONE VOICE AT A TIME</p>
      <div class="info__row">
        <span class="info__item"><svg viewBox="0 0 24 24"><path d="M12 2 C7 2 4 6 4 10 C4 16 12 22 12 22 C12 22 20 16 20 10 C20 6 17 2 12 2 Z" fill="#fff"/><circle cx="12" cy="10" r="3" fill="#111"/></svg>48 Cadence Road Riverton Victoria</span>
        <span class="info__item"><svg viewBox="0 0 24 24"><path d="M6 2 L10 3 L11 8 L8 10 C9 13 11 15 14 16 L16 13 L21 14 L22 18 C20 21 17 22 13 20 C8 17 5 13 3 8 C2 5 3 3 6 2 Z" fill="#fff"/></svg>P 1300 555 017</span>
      </div>
      <div class="info__row info__row--small">
        <span class="info__item"><svg viewBox="0 0 24 24"><circle cx="12" cy="12" r="10" fill="#fff"/></svg>The Melody Loft/melodyloft page</span>
        <span class="info__item"><svg viewBox="0 0 24 24"><circle cx="12" cy="12" r="10" fill="#fff"/></svg>Follow @the_melody_loft</span>
      </div>
    </footer>
  </div>
</div>
</body>
</html>
```